We need a full website with logo/graphics/woocommerce for hemp-based company

This site will be velmorix.com. It is a website featuring the fact we are the only manufacturer to produce CBDP and THCP. It should be great on mobile and desktop. We will pay for any extensions needed and while it should be a simple site:

About Us
About the Laboratory
About CBDP
About THCP
Shop
Contact Us

Only 4 products on the site.

It can be wordpress or joomla. Your choice. You must install the final website on our server. We agree to pay for monthly support that must be submitted in your quote.

He have a great graphics designer that will assist keeping colors and graphics clean according to your specifications.

Industry/Entity Type

Hemp CBD THC

Coding

Coded - Design and coding required

Number of Pages Required

5+ page

Requirements
Must have
• A simple clean layout

```html
<!DOCTYPE html>
<html lang="en">
<head>
<meta charset="utf-8">
<title>Velmorix — The Next Revolution in Cannabinoids</title>
<link rel="stylesheet" href="https://fonts.googleapis.com/css2?family=Roboto:ital,wght@0,400;0,500;0,700;1,400&display=swap">
<style>
:root{
  --green:#12a15a;
  --green-dark:#0e8a4c;
  --ink:#2b2b2b;
  --text:#6b6b6b;
  --light:#f4f4f4;
  --footer:#232323;
  --white:#ffffff;
  --logo-bg:#d7ecef;
}
*{box-sizing:border-box;margin:0;padding:0}
html,body{width:1200px;height:4870px;overflow:hidden}
body{font-family:"Roboto",Arial,sans-serif;color:var(--ink);background:var(--white);position:relative}
.btn-outline{position:absolute;display:flex;align-items:center;justify-content:center;border:2px solid var(--green);color:var(--green);font-weight:700;font-size:13px;letter-spacing:.2px;background:var(--white)}

/* header */
.site-header{position:absolute;left:0;top:0;width:1200px;height:128px;background:var(--green)}
.logo-box{position:absolute;left:111px;top:0;width:137px;height:136px;background:var(--logo-bg);display:flex;flex-direction:column;align-items:center;padding-top:18px;z-index:3}
.logo-name{font-weight:700;font-size:19px;color:var(--green)}
.logo-dot{width:56px;height:56px;border-radius:50%;background:var(--green);margin-top:16px}
.search{position:absolute;left:546px;top:19px;width:354px;height:47px;border-radius:24px;background:var(--white);font-size:14px;color:#777;padding:15px 0 0 24px}
.search-btn{position:absolute;right:4px;top:4px;width:39px;height:39px;border-radius:50%;background:var(--green);display:flex;align-items:center;justify-content:center}
.cart-icon{position:absolute;left:924px;top:19px;width:50px;height:50px;border-radius:50%;border:2px solid var(--white);display:flex;align-items:center;justify-content:center}
.cart-label{position:absolute;left:988px;top:34px;font-size:14px;font-weight:700;color:var(--white)}
.main-nav{position:absolute;left:326px;top:90px;display:flex;gap:22px;font-size:14px;font-weight:500;color:var(--white)}
.nav-marker{position:absolute;left:337px;top:112px;width:0;height:0;border-left:11px solid transparent;border-right:11px solid transparent;border-bottom:16px solid var(--white)}

/* hero */
.hero{position:absolute;left:0;top:128px;width:1200px;height:622px;background:linear-gradient(100deg,#4a5e42 0%,#6b8260 35%,#8fa088 60%,#5d7352 100%)}
.hero-panel{position:absolute;left:0;top:148px;width:682px;height:297px;background:rgba(30,40,30,.55)}
.hero-title{position:absolute;left:86px;top:30px;font-size:52px;line-height:51px;font-weight:700;color:var(--white)}
.hero-btn{position:absolute;left:87px;top:208px;width:130px;height:49px;background:var(--green);color:var(--white);font-size:14px;font-weight:700;display:flex;align-items:center;justify-content:center}
.hero-arrow{position:absolute;top:519px;width:44px;height:44px;border-radius:50%;background:rgba(25,25,25,.75);display:flex;align-items:center;justify-content:center}

/* products */
.section-title{position:absolute;left:0;width:1200px;text-align:center;font-size:34px;font-weight:500;color:var(--ink)}
.products{position:absolute;left:108px;top:918px;display:flex;gap:3px}
.product-card{width:243px;height:275px;position:relative;text-align:center}
.product-card .photo{height:178px}
.product-card h3{font-size:14px;font-weight:700;margin-top:18px}
.product-card p{font-size:10px;color:#555;margin-top:10px}
.product-card .price{font-size:14px;font-weight:700;color:var(--green);margin-top:12px}

/* about */
.about-photo{position:absolute;left:111px;top:1389px;width:488px;height:425px;background:linear-gradient(150deg,#6c73c8 0%,#5d8a4e 40%,#3f6a34 70%,#b8c9a0 100%)}
.about-box{position:absolute;left:557px;top:1425px;width:532px;height:352px;background:var(--green);color:var(--white);padding:30px 38px}
.about-box h2{font-size:34px;font-weight:500}
.about-box p{font-size:13px;line-height:22.5px;margin-top:14px}
.btn-white{position:absolute;left:42px;top:263px;width:135px;height:44px;border:2px solid var(--white);color:var(--white);font-size:13px;font-weight:700;display:flex;align-items:center;justify-content:center}

/* cannabinoids */
.body-system{position:absolute;left:0;top:1918px;width:1200px;height:522px;background:var(--light)}
.body-system h2{position:absolute;top:94px;width:1200px;text-align:center;font-size:34px;font-weight:500;line-height:40px}
.body-system .lead{position:absolute;top:190px;width:1200px;text-align:center;font-size:13px;color:#555}
.component{position:absolute;top:234px;width:260px;text-align:center;font-size:16px;line-height:25px;font-weight:500}
.component .icon{width:126px;height:126px;border-radius:50%;background:var(--green);margin:0 auto 14px}

/* feature rows */
.feature{position:absolute;left:0;width:1200px;height:514px}
.feature .photo{position:absolute;top:0;width:600px;height:514px}
.feature .copy{position:absolute;top:58px;width:432px}
.feature h2{font-size:34px;font-weight:500}
.feature p{font-size:13px;line-height:25.7px;color:var(--text);margin-top:16px}
.feature .btn-outline{position:relative;margin-top:30px;width:130px;height:46px}
.feature.right .copy{text-align:right}
.feature.right .btn-outline{margin-left:auto}

/* testimonials */
.testimonial{position:absolute;top:4160px;width:330px}
.quote-mark{font-size:64px;font-weight:700;color:var(--green);line-height:50px;font-family:Georgia,serif}
.testimonial p{font-size:12.5px;font-style:italic;color:#777;line-height:22px;margin-top:14px}
.testimonial .name{font-size:17px;font-weight:500;color:#555;margin-top:22px}
.slide-arrow{position:absolute;top:4270px}

/* footer */
.site-footer{position:absolute;left:0;top:4522px;width:1200px;height:348px;background:var(--footer);color:var(--white)}
.footer-logo{position:absolute;left:106px;top:82px;width:108px;height:108px;background:var(--logo-bg);display:flex;flex-direction:column;align-items:center;padding-top:14px}
.footer-logo .logo-name{font-size:15px}
.footer-logo .logo-dot{width:44px;height:44px;margin-top:10px}
.footer-legal{position:absolute;left:106px;top:205px;font-size:12px;line-height:21px}
.footer-col{position:absolute;top:80px}
.footer-col h4{font-size:19px;font-weight:500;margin-bottom:20px}
.footer-col li{list-style:none;font-size:13px;line-height:25.5px}
.contact-line{display:flex;gap:14px;font-size:13px;line-height:20px;margin-bottom:14px}
.contact-line svg{flex:none;margin-top:3px}
</style>
</head>
<body>

<header class="site-header">
  <div class="logo-box"><span class="logo-name">Velmorix</span><span class="logo-dot"></span></div>
  <div class="search">Enter your keyword
    <span class="search-btn"><svg width="16" height="16" viewBox="0 0 16 16"><circle cx="6.5" cy="6.5" r="4.5" fill="none" stroke="#fff" stroke-width="2"/><line x1="10" y1="10" x2="14" y2="14" stroke="#fff" stroke-width="2.4" stroke-linecap="round"/></svg></span>
  </div>
  <div class="cart-icon"><svg width="20" height="18" viewBox="0 0 20 18"><path d="M1 2h3l2 9h10l2-7H5" fill="#fff" stroke="#fff" stroke-width="1.5" stroke-linejoin="round"/><circle cx="8" cy="15" r="1.6" fill="#fff"/><circle cx="15" cy="15" r="1.6" fill="#fff"/></svg></div>
  <div class="cart-label">My Cart : 0.00</div>
  <nav class="main-nav"><span>HOME</span><span>ABOUT US</span><span>ABOUT THE LABORATORY</span><span>ABOUT CBDP</span><span>ABOUT THCP</span><span>SHOP</span><span>CONTACT US</span></nav>
  <div class="nav-marker"></div>
</header>

<section class="hero" role="img" aria-label="Hand holding a green dropper bottle in front of hemp plants">
  <div class="hero-panel">
    <h1 class="hero-title">VELMORIX<br>THE NEXT REVOLUTION<br>IN CANNABINOIDS</h1>
    <div class="hero-btn">SHOP NOW</div>
  </div>
  <div class="hero-arrow" style="left:547px"><svg width="12" height="18" viewBox="0 0 12 18"><path d="M9 2 3 9l6 7" fill="none" stroke="#fff" stroke-width="2.4"/></svg></div>
  <div class="hero-arrow" style="left:605px"><svg width="12" height="18" viewBox="0 0 12 18"><path d="m3 2 6 7-6 7" fill="none" stroke="#fff" stroke-width="2.4"/></svg></div>
</section>

<h2 class="section-title" style="top:844px">OUR PRODUCTS</h2>
<div class="products">
  <article class="product-card" style="background:#f2ebeb"><div class="photo" role="img" aria-label="Oil bottles with a vape pen"></div><h3>Lorem ipsum dolor</h3><p>Nemo enim ipsam voluptatem quia</p><div class="price">$25.00</div></article>
  <article class="product-card" style="background:#faf6ee"><div class="photo" role="img" aria-label="Amber dropper bottle with a vape pen"></div><h3>Lorem ipsum dolor</h3><p>Nemo enim ipsam voluptatem quia</p><div class="price">$25.00</div></article>
  <article class="product-card" style="background:#f2eded"><div class="photo" role="img" aria-label="Set of vape pens"></div><h3>Lorem ipsum dolor</h3><p>Nemo enim ipsam voluptatem quia</p><div class="price">$25.00</div></article>
  <article class="product-card" style="background:#fbf7ef"><div class="photo" role="img" aria-label="Three orange dropper bottles"></div><h3>Lorem ipsum dolor</h3><p>Nemo enim ipsam voluptatem quia</p><div class="price">$25.00</div></article>
</div>
<div class="btn-outline" style="left:506px;top:1230px;width:188px;height:55px">SHOP ALL PRODUCTS</div>

<div class="about-photo" role="img" aria-label="Gloved hands dropping oil into a small glass bottle near hemp leaves"></div>
<section class="about-box">
  <h2>About us</h2>
  <p>Velmorix is the first lab to be able to make the minor cannabinoids TCHP and CBDP in bulk batches. These canniboids were are 2 of the 150 cannabinoids found in the hemp plant and 2 of the ones found in the smallest amounts. Although most cannabis strains contain very small amounts of THCP and CBDP, the isolation of these phytocannabinoids have the potential to change the way we think about cannabinoids altogether.</p>
  <div class="btn-white">LEARN MORE</div>
</section>

<section class="body-system">
  <h2>How do these cannabinoids<br>affect the human body?</h2>
  <p class="lead">THCP's effects are produced by the endocannabinoid system (ECS). The ECS is made up of three components</p>
  <div class="component" style="left:144px"><div class="icon" role="img" aria-label="Endocannabinoids icon"></div>Endocannabinoids</div>
  <div class="component" style="left:469px"><div class="icon" role="img" aria-label="Cannabinoid receptors icon"></div>Cannabinoid Receptors 1<br>and 2 (CB1 and CB2)</div>
  <div class="component" style="left:796px"><div class="icon" role="img" aria-label="Enzymes icon"></div>Enzymes</div>
</section>

<section class="feature" style="top:2440px">
  <div class="photo" style="left:0;background:linear-gradient(120deg,#cfd8de 0%,#eef1f3 45%,#9aa7b0 100%)" role="img" aria-label="Scientist taking notes beside laboratory distillation equipment"></div>
  <div class="copy" style="left:656px;top:56px">
    <h2>Laboratory</h2>
    <p>Lorem ipsum dolor sit amet, consectetur adipiscing elit, sed do eiusmod tempor incididunt ut labore et dolore magna aliqua. Ut enim ad minim veniam, quis nostrud exercitation ullamco laboris nisi ut aliquip ex ea commodo consequat. Duis aute irure dolor in reprehenderit in voluptate velit esse cillum dolore eu fugiat nulla pariatur. Excepteur sint occaecat cupidatat non proident, sunt in culpa qui officia deserunt mollit anim id est laborum. Lorem ipsum dolor sit amet, consectetur adipiscing elit, sed do eiusmod tempor incididunt ut labore et dolore magna aliqua. Ut enim ad minim veniam, quis nostrud exercitation ullamco laboris nisi ut aliquip ex ea commodo consequat.</p>
    <div class="btn-outline">LEARN MORE</div>
  </div>
</section>

<section class="feature right" style="top:2954px">
  <div class="copy" style="left:110px;top:58px">
    <h2>CBDP</h2>
    <p>Lorem ipsum dolor sit amet, consectetur adipiscing elit, sed do eiusmod tempor incididunt ut labore et dolore magna aliqua. Ut enim ad minim veniam, quis nostrud exercitation ullamco laboris nisi ut aliquip ex ea commodo consequat. Duis aute irure dolor in reprehenderit in voluptate velit esse cillum dolore eu fugiat nulla pariatur. Excepteur sint occaecat cupidatat non proident, sunt in culpa qui officia deserunt mollit anim id est laborum. Lorem ipsum dolor sit amet, consectetur adipiscing elit, sed do eiusmod tempor incididunt ut labore et dolore magna aliqua. Ut enim ad minim veniam, quis nostrud exercitation ullamco laboris nisi ut aliquip ex ea commodo consequat.</p>
    <div class="btn-outline">LEARN MORE</div>
  </div>
  <div class="photo" style="left:600px;background:linear-gradient(135deg,#8a6a4c 0%,#b0916f 45%,#6e5038 100%)" role="img" aria-label="Hemp leaf and dark dropper bottle on a wooden stump"></div>
</section>

<section class="feature" style="top:3468px">
  <div class="photo" style="left:0;background:linear-gradient(160deg,#e9e3d2 0%,#a8b98c 45%,#5f7a45 100%)" role="img" aria-label="Woman holding an oil bottle in a hemp field"></div>
  <div class="copy" style="left:656px;top:56px">
    <h2>THCP</h2>
    <p>Lorem ipsum dolor sit amet, consectetur adipiscing elit, sed do eiusmod tempor incididunt ut labore et dolore magna aliqua. Ut enim ad minim veniam, quis nostrud exercitation ullamco laboris nisi ut aliquip ex ea commodo consequat. Duis aute irure dolor in reprehenderit in voluptate velit esse cillum dolore eu fugiat nulla pariatur. Excepteur sint occaecat cupidatat non proident, sunt in culpa qui officia deserunt mollit anim id est laborum. Lorem ipsum dolor sit amet, consectetur adipiscing elit, sed do eiusmod tempor incididunt ut labore et dolore magna aliqua. Ut enim ad minim veniam, quis nostrud exercitation ullamco laboris nisi ut aliquip ex ea commodo consequat.</p>
    <div class="btn-outline">LEARN MORE</div>
  </div>
</section>

<h2 class="section-title" style="top:4075px">What Our Customers Are Saying?</h2>
<svg class="slide-arrow" style="left:42px" width="18" height="32" viewBox="0 0 18 32"><path d="M15 2 3 16l12 14" fill="none" stroke="#555" stroke-width="2.5"/></svg>
<svg class="slide-arrow" style="left:1138px" width="18" height="32" viewBox="0 0 18 32"><path d="m3 2 12 14L3 30" fill="none" stroke="#555" stroke-width="2.5"/></svg>
<div class="testimonial" style="left:111px"><div class="quote-mark">&ldquo;</div><p>"Lorem ipsum dolor sit amet, consectetur adipiscing elit, sed do eiusmod tempor incididunt ut labore et dolore magna aliqua. Ut enim ad minim veniam, quis nostrud exercitation ullamco laboris nisi ut Lorem ipsum dolor sit amet, consectetur adipiscing elit, sed do eiusmod tempor incididunt ut labore et dolore magna aliqua."</p><div class="name">John Doe</div></div>
<div class="testimonial" style="left:457px"><div class="quote-mark">&ldquo;</div><p>"Lorem ipsum dolor sit amet, consectetur adipiscing elit, sed do eiusmod tempor incididunt ut labore et dolore magna aliqua. Ut enim ad minim veniam, quis nostrud exercitation ullamco laboris nisi ut Lorem ipsum dolor sit amet, consectetur adipiscing elit, sed do eiusmod tempor incididunt ut labore et dolore magna aliqua."</p><div class="name">John Doe</div></div>
<div class="testimonial" style="left:803px"><div class="quote-mark">&ldquo;</div><p>"Lorem ipsum dolor sit amet, consectetur adipiscing elit, sed do eiusmod tempor incididunt ut labore et dolore magna aliqua. Ut enim ad minim veniam, quis nostrud exercitation ullamco laboris nisi ut Lorem ipsum dolor sit amet, consectetur adipiscing elit, sed do eiusmod tempor incididunt ut labore et dolore magna aliqua."</p><div class="name">John Doe</div></div>

<footer class="site-footer">
  <div class="footer-logo"><span class="logo-name">Velmorix</span><span class="logo-dot"></span></div>
  <div class="footer-legal">@ 2021 Company name All Rights<br>Reserved<br>Contact Us<br>Terms &amp; Conditions</div>
  <div class="footer-col" style="left:374px"><h4>Products</h4><ul><li>Lorem ipsum</li><li>Dolor sit amet,</li><li>Consectetur adip</li><li>Iscing elit</li><li>Lorem ipsum</li><li>Dolor sit amet,</li></ul></div>
  <div class="footer-col" style="left:599px"><h4>Quick Links</h4><ul><li>Shop</li><li>Quiz</li><li>Learn</li><li>About</li><li>FAQ</li><li>Shipping &amp; Refund</li><li>Contact Us</li></ul></div>
  <div class="footer-col" style="left:822px;width:300px"><h4>Contact Us</h4>
    <div style="color:var(--green);font-size:13px;margin-bottom:14px">Tarnwell LLC</div>
    <div class="contact-line"><svg width="11" height="14" viewBox="0 0 11 14"><path d="M5.5 0C2.5 0 0 2.3 0 5.3 0 9 5.5 14 5.5 14S11 9 11 5.3C11 2.3 8.5 0 5.5 0Z" fill="#12a15a"/><circle cx="5.5" cy="5.3" r="2" fill="#232323"/></svg><span>Lorem ipsum dolor sit amet,<br>consectetur</span></div>
    <div class="contact-line"><svg width="13" height="13" viewBox="0 0 13 13"><path d="M3 0 5 3 3.6 4.6a8 8 0 0 0 4.8 4.8L10 8l3 2-1.4 2.6C6 13 0 7 .4 1.4Z" fill="#12a15a"/></svg><span>Phone: +1 888 888 8888</span></div>
    <div class="contact-line"><svg width="14" height="11" viewBox="0 0 14 11"><rect width="14" height="11" rx="1" fill="#12a15a"/><path d="m1 1 6 5 6-5" fill="none" stroke="#232323" stroke-width="1.3"/></svg><span>Email: info@companyname.com</span></div>
  </div>
</footer>

</body>
</html>
```